Business Card Design Project for an English Teacher

I need a business card design for my new job.
I'd like to start teaching English as a freelance.
My students will be children, teenager, and adults, who don't like or hesitate to study English and I would like to open a door to the new world for them.

I'd like to put the information below;
[right side]
1. name
2. mail address
3. mobile number
4. website or facebook page

[back]
1.my message: Feel free at asking me anything about my classes

2.lesson list such as:
price: 3150 yen ~

calsses:
kids class( mum& dad can join) ... 30 minutes / 45 minutes
students (over age 13).... 60minutes / 90 minutes
Adult (over age 19) .... 60 minutes / 90 minutes

3. I'll have both Web Lesson and Face to Face Lesson

4. Free trial lesson

Target Market(s)

My students will be children, teenager, and adults, who don't like or hesitate to study English

Industry/Entity Type

Business

Requirements
Must have
• designed both side

```html
<!DOCTYPE html>
<html lang="en">
<head>
<meta charset="utf-8">
<title>English Instructor – Business Card</title>
<link href="https://fonts.googleapis.com/css2?family=Saira+Condensed:wght@300;400;500;600;700&display=swap" rel="stylesheet">
<style>
  :root {
    --page: #ffffff;
    --blue-light: #0b66a8;
    --blue-dark: #064a7c;
    --red: #d60008;
    --red-dark: #9a0006;
    --silver-dark: #d9d9d9;
    --ink: #0d0d0d;
    --paper: #ffffff;
  }
  html, body {
    margin: 0;
    width: 1200px;
    height: 900px;
    overflow: hidden;
    background: var(--page);
  }
  .canvas {
    position: relative;
    width: 1200px;
    height: 900px;
  }
  .card {
    position: absolute;
    top: 97px;
    width: 378px;
    height: 661px;
    overflow: hidden;
    font-family: "Saira Condensed", "Arial Narrow", sans-serif;
    color: var(--paper);
  }
  .card--front { left: 180px; }
  .card--back { left: 587px; }
  .card__bg {
    position: absolute;
    inset: 0;
    width: 100%;
    height: 100%;
  }
  .line {
    position: absolute;
    left: 33px;
    width: 315px;
    height: 3px;
    background: var(--paper);
  }
  .text {
    position: absolute;
    left: 0;
    width: 100%;
    text-align: center;
    line-height: 1;
    margin: 0;
    white-space: nowrap;
  }
  .text--ink { color: var(--ink); }

  /* front */
  .role { top: 154px; font-size: 35px; font-weight: 600; letter-spacing: 1.5px; }
  .name {
    font-weight: 400;
    font-size: 146px;
    letter-spacing: 3px;
  }
  .name--first { top: 186px; }
  .name--last { top: 294px; }
  .label-contact { top: 431px; font-size: 31px; font-weight: 700; }
  .phone { top: 472px; font-size: 44px; font-weight: 400; letter-spacing: 3px; }
  .email { top: 534px; font-size: 29px; font-weight: 400; letter-spacing: 2px; }
  .website { top: 624px; font-size: 25px; font-weight: 500; letter-spacing: 2px; }

  /* back */
  .ask { top: 20px; font-size: 46px; font-weight: 600; letter-spacing: 2px; }
  .ask-sub { top: 64px; font-size: 31px; font-weight: 600; letter-spacing: 1px; }
  .price {
    top: 92px;
    font-size: 136px;
    font-weight: 500;
    letter-spacing: 4px;
  }
  .label-classes { top: 228px; font-size: 30px; font-weight: 700; letter-spacing: 1px; }
  .class-name { font-size: 25px; font-weight: 600; letter-spacing: 0.5px; }
  .class-time { font-size: 36px; font-weight: 600; letter-spacing: 1.5px; }
  .kids-name { top: 274px; }
  .kids-time { top: 301px; }
  .students-name { top: 347px; }
  .students-time { top: 375px; }
  .adult-name { top: 420px; }
  .adult-time { top: 449px; }
  .format { top: 502px; font-size: 27px; font-weight: 600; letter-spacing: 0.5px; }
  .trial { top: 546px; font-size: 38px; font-weight: 700; }
</style>
</head>
<body>
<main class="canvas">

  <section class="card card--front" aria-label="Front of business card">
    <svg class="card__bg" viewBox="0 0 378 661" aria-hidden="true">
      <defs>
        <radialGradient id="frontBlue" cx="50%" cy="50%" r="65%">
          <stop offset="0" stop-color="#0b66a8"/>
          <stop offset="1" stop-color="#064a7c"/>
        </radialGradient>
        <linearGradient id="frontRed" x1="0" y1="0" x2="1" y2="0.6">
          <stop offset="0" stop-color="#d60008"/>
          <stop offset="1" stop-color="#9a0006"/>
        </linearGradient>
        <linearGradient id="frontSilver" x1="0" y1="0" x2="1" y2="0">
          <stop offset="0" stop-color="#ffffff"/>
          <stop offset="1" stop-color="#d9d9d9"/>
        </linearGradient>
      </defs>
      <rect width="378" height="661" fill="url(#frontBlue)"/>
      <polygon points="55,0 378,0 378,36 232,85" fill="url(#frontSilver)"/>
      <polygon points="0,0 55,0 232,85 0,165" fill="url(#frontRed)"/>
    </svg>

    <p class="text role">ENGLISH INSTRUCTOR</p>
    <div class="line" style="top:200px"></div>
    <h1 class="text name name--first">EMIKO</h1>
    <h1 class="text name name--last">SATO</h1>
    <div class="line" style="top:422px"></div>
    <p class="text text--ink label-contact">CONTACT</p>
    <div class="line" style="top:470px"></div>
    <p class="text phone">080-****-****</p>
    <p class="text email">emiko****@mailhub.com</p>
    <p class="text website">www.emikosato.com</p>
  </section>

  <section class="card card--back" aria-label="Back of business card">
    <svg class="card__bg" viewBox="0 0 378 661" aria-hidden="true">
      <defs>
        <radialGradient id="backBlue" cx="50%" cy="45%" r="65%">
          <stop offset="0" stop-color="#0b66a8"/>
          <stop offset="1" stop-color="#064a7c"/>
        </radialGradient>
        <linearGradient id="backRed" x1="0" y1="0" x2="1" y2="0">
          <stop offset="0" stop-color="#d60008"/>
          <stop offset="1" stop-color="#9a0006"/>
        </linearGradient>
        <linearGradient id="backSilver" x1="0" y1="0" x2="1" y2="0">
          <stop offset="0" stop-color="#d9d9d9"/>
          <stop offset="1" stop-color="#ffffff"/>
        </linearGradient>
      </defs>
      <rect width="378" height="661" fill="url(#backBlue)"/>
      <polygon points="0,648 188,624 206,661 0,661" fill="url(#backSilver)"/>
      <polygon points="188,624 378,603 378,661 206,661" fill="url(#backRed)"/>
    </svg>

    <p class="text ask">FEEL FREE TO ASK</p>
    <p class="text ask-sub">FOR MORE INFORMATION</p>
    <div class="line" style="top:101px"></div>
    <p class="text price">¥3150</p>
    <div class="line" style="top:222px"></div>
    <p class="text text--ink label-classes">CLASSES</p>
    <div class="line" style="top:260px"></div>

    <p class="text class-name kids-name">Kids Class</p>
    <p class="text class-time kids-time">30/45 min</p>
    <p class="text class-name students-name">Students (Over age 13)</p>
    <p class="text class-time students-time">60/90 min</p>
    <p class="text class-name adult-name">Adult (Over age 19)</p>
    <p class="text class-time adult-time">60/90 min</p>

    <div class="line" style="top:493px"></div>
    <p class="text format">WEB / FACE TO FACE LESSON</p>
    <div class="line" style="top:537px"></div>
    <p class="text text--ink trial">GET FREE TRIAL LESSON</p>
  </section>

</main>
</body>
</html>
```